Financial Planning business needs a new Business Card design

We need a business card design for an Australian financial planning business. I am looking for a clean simple design

Target Market(s)

People aged 25-40

Industry/Entity Type

Financial Service

Contact Information for Business Card

On the front of the card we need the following information:
Name: Derek Holloway (First Name Green: #006838 and last name Grey: #414042)
Position: Financial Adviser
Qualifications: BEc(Hons), AdDipFS(FP), Dip FMBM, AFP®
Mobile: 0437 215 604
Email: derek@mondlane.com.au

On the back of the card we need:
Postal address: PO BOX 5736, PERTH BC, WA 6849
Website: www.mondlane.com.au
Text: AFS Licence No. 518624

The fields need to be able to be edited.

Font styles to use
Sans Serif

Requirements
Must have
• Information listed above

```html
<!DOCTYPE html>
<html lang="en">
<head>
<meta charset="utf-8">
<title>Mondlane Business Card</title>
<link href="https://fonts.googleapis.com/css2?family=Open+Sans:wght@400;600;700&display=swap" rel="stylesheet">
<style>
  :root {
    --green: #006838;
    --grey: #414042;
    --text: #3a3a3c;
    --card: #ffffff;
    --backdrop: #e9e7e4;
  }
  html, body {
    margin: 0;
    padding: 0;
    width: 1200px;
    height: 1000px;
    overflow: hidden;
    background: var(--backdrop);
    font-family: "Open Sans", Arial, sans-serif;
  }
  .card {
    position: absolute;
    left: 265px;
    width: 665px;
    height: 397px;
    background: var(--card);
    box-shadow: 0 2px 8px rgba(0,0,0,0.15);
    overflow: hidden;
  }
  .card--front { top: 73px; }
  .card--back { top: 533px; height: 396px; }

  .brand {
    position: absolute;
    left: 45px;
    top: 176px;
    width: 285px;
    display: flex;
    align-items: center;
    gap: 10px;
    font-weight: 700;
    font-size: 38px;
    letter-spacing: 0.5px;
    color: var(--green);
    line-height: 1;
    white-space: nowrap;
  }
  .brand__mark {
    flex: none;
    width: 12px;
    height: 12px;
    border-radius: 50%;
    background: var(--green);
  }

  .divider {
    position: absolute;
    left: 354px;
    width: 2px;
    background: var(--grey);
  }
  .card--front .divider { top: 118px; height: 140px; }
  .card--back .divider { top: 170px; height: 58px; }

  .person {
    position: absolute;
    left: 395px;
    top: 112px;
    color: var(--text);
    font-size: 16px;
    line-height: 22px;
  }
  .person__name {
    font-size: 21px;
    line-height: 30px;
    color: var(--grey);
    text-transform: uppercase;
    margin: 0;
    font-weight: 400;
  }
  .person__first { color: var(--green); font-weight: 600; }
  .person__role, .person__quals { margin: 0; }
  .contact {
    list-style: none;
    margin: 12px 0 0;
    padding: 0;
  }
  .contact li {
    display: flex;
    align-items: center;
    gap: 8px;
    line-height: 23px;
  }
  .contact svg { width: 14px; height: 12px; fill: var(--green); }

  .band {
    position: absolute;
    left: 0;
    bottom: 0;
    width: 665px;
    height: 27px;
  }

  .company {
    position: absolute;
    left: 372px;
    top: 165px;
    margin: 0;
    font-style: normal;
    font-size: 16px;
    line-height: 22px;
    color: var(--text);
    letter-spacing: 0.2px;
    white-space: nowrap;
  }
</style>
</head>
<body>

<section class="card card--front">
  <div class="brand"><span class="brand__mark"></span>MONDLANE</div>
  <div class="divider"></div>
  <div class="person">
    <h1 class="person__name"><span class="person__first">Derek</span> Holloway</h1>
    <p class="person__role">Financial Adviser</p>
    <p class="person__quals">BEc(Hons), AdDipFS(FP),<br>Dip FMBM, AFP®</p>
    <ul class="contact">
      <li>
        <svg viewBox="0 0 14 12" aria-hidden="true"><path d="M1 3 C1 1 3 0 7 0 C11 0 13 1 13 3 L10 4 L9 2.5 L5 2.5 L4 4 Z M3 5 L11 5 L13 11 L1 11 Z"/></svg>
        0437 215 604
      </li>
      <li>
        <svg viewBox="0 0 14 12" aria-hidden="true"><path d="M0 1 L14 1 L14 11 L0 11 Z M1 2 L7 7 L13 2 Z" fill-rule="evenodd"/></svg>
        derek@mondlane.com.au
      </li>
    </ul>
  </div>
  <svg class="band" viewBox="0 0 665 27" aria-hidden="true">
    <polygon points="0,0 348,0 300,27 0,27" fill="var(--green)"/>
    <polygon points="364,0 665,0 665,27 316,27" fill="var(--grey)"/>
  </svg>
</section>

<section class="card card--back">
  <div class="brand"><span class="brand__mark"></span>MONDLANE</div>
  <div class="divider"></div>
  <address class="company">
    AFS Licence No. 518624<br>
    www.mondlane.com.au<br>
    PO BOX 5736, PERTH BC, WA 6849
  </address>
</section>

</body>
</html>
```